Infographic for CPA Firm Lead Magnet

I need a one page infographic for a lead magnet for my CPA firm. The name of the lead magnet will be "Hidden Perks Nobody Mentions About Ledger Pros". The lead magnet will need to have my firm logo (attached) on it, or watermarked on it. The attached Excel file has the three content categories which are the content basis for the infographic. My website is cedarlinecpa.com to give you a better sense of my branding. Feel free to use whichever logo version you think is appropriate, and to take whatever information you deem appropriate from my website.

Target Market(s)

Business owners/entrepreneurs

Industry/Entity Type

Accounting

Font styles to use
Sans Serif

Colors

Designer to choose colors to be used in the design.

Requirements
Must have
• Must have each category and item listed on the Excel file. Must also have my logo or my logo watermarked.

```html
<!DOCTYPE html>
<html lang="en">
<head>
<meta charset="utf-8">
<title>Hidden Perks Nobody Mentions About Ledger Pros — Cedarline CPA</title>
<link rel="stylesheet" href="https://fonts.googleapis.com/css2?family=Source+Sans+3:wght@400;600&display=swap">
<style>
  :root {
    --paper: #ffffff;
    --ink: #1d1d1f;
    --navy: #1f3a7a;
    --spine: #2a3442;
    --orange: #f5a75c;
    --pink: #ef5f83;
    --magenta: #e6379d;
    --purple: #b653d9;
    --violet: #9b6ae0;
    --sky: #5cc2f0;
    --lime: #82e05e;
    --red: #d63a33;
    --slate: #34466e;
    --olive: #7ea52a;
    --mint: #4fdc8c;
    --tang: #f0802d;
    --charcoal: #474b50;
  }
  html, body {
    margin: 0;
    width: 1200px;
    height: 1181px;
    overflow: hidden;
    background: var(--paper);
  }
  .infographic {
    display: block;
    width: 1200px;
    height: 1181px;
    font-family: "Source Sans 3", sans-serif;
  }
  .pill-label { font-size: 14.5px; fill: var(--ink); font-weight: 400; }
  .pill-num { font-size: 13px; fill: var(--ink); }
  .firm-name { font-size: 30px; font-weight: 600; fill: var(--navy); letter-spacing: 2px; }
  .firm-sub { font-size: 16px; font-weight: 600; fill: var(--navy); letter-spacing: 2px; }
  .magnet-title { font-size: 12.5px; font-weight: 600; fill: var(--ink); }
  .service { font-size: 15px; }
  .c-red { fill: var(--red); }
  .c-slate { fill: var(--slate); }
  .c-olive { fill: var(--olive); }
  .c-mint { fill: var(--mint); }
  .c-tang { fill: var(--tang); }
</style>
</head>
<body>
<svg class="infographic" viewBox="0 0 768 757" xmlns="http://www.w3.org/2000/svg">

  <!-- firm name and lead magnet title -->
  <g class="firm-mark">
    <rect x="26" y="134" width="9" height="9" fill="var(--navy)"/>
    <text class="firm-name" x="40" y="160">CEDARLINE</text>
    <text class="firm-sub" x="41" y="181">CPA</text>
  </g>
  <g class="lead-magnet">
    <text class="magnet-title" x="26" y="205">Hidden Perks Nobody Mentions</text>
    <text class="magnet-title" x="26" y="220">About Ledger Pros</text>
  </g>

  <!-- timeline spine -->
  <line x1="487" y1="14" x2="487" y2="356" stroke="var(--spine)" stroke-width="3"/>

  <!-- 01 -->
  <g class="step step-right">
    <circle cx="487" cy="36" r="8" fill="var(--orange)"/>
    <circle cx="505" cy="36" r="2.5" fill="var(--orange)"/>
    <polygon points="514,36 522,30 522,42" fill="var(--orange)"/>
    <rect x="520" y="14" width="156" height="44" rx="22" fill="var(--orange)"/>
    <circle cx="651" cy="36" r="17" fill="#fff"/>
    <text class="pill-label" x="535" y="41">1099 Issuance</text>
    <text class="pill-num" x="651" y="41" text-anchor="middle">01</text>
    <circle cx="700" cy="36" r="17" fill="var(--orange)"/>
  </g>

  <!-- 02 -->
  <g class="step step-left">
    <circle cx="487" cy="75" r="9" fill="var(--pink)"/>
    <circle cx="470" cy="75" r="2.5" fill="var(--pink)"/>
    <polygon points="467,75 459,69 459,81" fill="var(--pink)"/>
    <rect x="300" y="53" width="161" height="44" rx="22" fill="var(--pink)"/>
    <circle cx="323" cy="75" r="17" fill="#fff"/>
    <text class="pill-num" x="323" y="80" text-anchor="middle">02</text>
    <text class="pill-label" x="348" y="70">Accounting &amp;</text>
    <text class="pill-label" x="348" y="87">Bookkeeping</text>
    <circle cx="271" cy="75" r="16" fill="var(--pink)"/>
  </g>

  <!-- 03 -->
  <g class="step step-right">
    <circle cx="487" cy="117" r="8" fill="var(--magenta)"/>
    <circle cx="505" cy="117" r="2.5" fill="var(--magenta)"/>
    <polygon points="514,117 522,111 522,123" fill="var(--magenta)"/>
    <rect x="520" y="95" width="156" height="44" rx="22" fill="var(--magenta)"/>
    <circle cx="651" cy="117" r="17" fill="#fff"/>
    <text class="pill-label" x="545" y="112">Financial</text>
    <text class="pill-label" x="545" y="130">Planning</text>
    <text class="pill-num" x="651" y="122" text-anchor="middle">03</text>
    <circle cx="700" cy="117" r="17" fill="var(--magenta)"/>
  </g>

  <!-- 04 & 05 -->
  <g class="step step-left">
    <polygon points="467,186 459,180 459,192" fill="var(--purple)"/>
    <rect x="300" y="164" width="161" height="44" rx="22" fill="var(--purple)"/>
    <circle cx="323" cy="186" r="17" fill="#fff"/>
    <text class="pill-num" x="323" y="191" text-anchor="middle">04</text>
    <text class="pill-label" x="352" y="191">Federal Taxes</text>
    <circle cx="271" cy="186" r="16" fill="var(--purple)"/>
  </g>
  <g class="step step-right">
    <polygon points="514,186 522,180 522,192" fill="var(--orange)"/>
    <rect x="520" y="164" width="156" height="44" rx="22" fill="var(--orange)"/>
    <circle cx="651" cy="186" r="17" fill="#fff"/>
    <text class="pill-label" x="535" y="191">Tax Planning</text>
    <text class="pill-num" x="651" y="191" text-anchor="middle">05</text>
    <circle cx="700" cy="186" r="17" fill="var(--orange)"/>
  </g>
  <circle cx="487" cy="186" r="12" fill="var(--navy)"/>

  <!-- 06 -->
  <g class="step step-right">
    <circle cx="487" cy="258" r="8" fill="var(--violet)"/>
    <circle cx="505" cy="258" r="2.5" fill="var(--violet)"/>
    <polygon points="514,258 522,252 522,264" fill="var(--violet)"/>
    <rect x="520" y="236" width="156" height="44" rx="22" fill="var(--violet)"/>
    <circle cx="651" cy="258" r="17" fill="#fff"/>
    <text class="pill-label" x="532" y="263">IRS Resolution</text>
    <text class="pill-num" x="651" y="263" text-anchor="middle">06</text>
    <circle cx="700" cy="258" r="17" fill="var(--violet)"/>
  </g>

  <!-- 07 -->
  <g class="step step-left">
    <circle cx="487" cy="300" r="9" fill="var(--sky)"/>
    <circle cx="470" cy="300" r="2.5" fill="var(--sky)"/>
    <polygon points="467,300 459,294 459,306" fill="var(--sky)"/>
    <rect x="300" y="278" width="161" height="44" rx="22" fill="var(--sky)"/>
    <circle cx="323" cy="300" r="17" fill="#fff"/>
    <text class="pill-num" x="323" y="305" text-anchor="middle">07</text>
    <text class="pill-label" x="354" y="305">State Taxes</text>
    <circle cx="271" cy="300" r="16" fill="var(--sky)"/>
  </g>

  <!-- 08 -->
  <g class="step step-right">
    <circle cx="487" cy="342" r="8" fill="var(--lime)"/>
    <circle cx="505" cy="342" r="2.5" fill="var(--lime)"/>
    <polygon points="514,342 522,336 522,348" fill="var(--lime)"/>
    <rect x="520" y="320" width="156" height="44" rx="22" fill="var(--lime)"/>
    <circle cx="651" cy="342" r="17" fill="#fff"/>
    <text class="pill-label" x="550" y="347">Payroll</text>
    <text class="pill-num" x="651" y="347" text-anchor="middle">08</text>
    <circle cx="700" cy="342" r="17" fill="var(--lime)"/>
  </g>

  <!-- journey arrow -->
  <line x1="155" y1="520" x2="650" y2="520" stroke="var(--charcoal)" stroke-width="4"/>
  <polygon points="672,520 646,508 646,532" fill="var(--charcoal)"/>

  <rect x="0" y="425" width="132" height="130" fill="var(--charcoal)" role="img" aria-label="Office building illustration"/>
  <rect x="668" y="460" width="100" height="96" fill="var(--charcoal)" role="img" aria-label="Illustration of a business owner working at a desk"/>

  <!-- services above the arrow -->
  <g class="services-upper service" text-anchor="end">
    <text class="c-red" transform="translate(203,500) rotate(49)">Software Consulting &amp; Implementation</text>
    <text class="c-slate" transform="translate(246,505) rotate(49)">Choice of Legal Structure Consulting</text>
    <text class="c-olive" transform="translate(287,500) rotate(49)">Business Management Reports</text>
    <text class="c-mint" transform="translate(331,498) rotate(49)">Cash Flow Management</text>
    <text class="c-tang" transform="translate(372,500) rotate(49)">Performance Tracking</text>
    <text class="c-slate" transform="translate(414,497) rotate(49)">Profitability Analysis</text>
    <text class="c-red" transform="translate(457,497) rotate(49)">Sales Tax Returns</text>
    <text class="c-olive" transform="translate(499,497) rotate(49)">Business Plans</text>
    <text class="c-tang" transform="translate(546,497) rotate(49)">Benchmarking</text>
    <text class="c-slate" transform="translate(586,497) rotate(49)">Local Taxes</text>
    <text class="c-mint" transform="translate(628,500) rotate(49)">Dashboards</text>
  </g>

  <!-- services below the arrow -->
  <g class="services-lower service" text-anchor="end">
    <text class="c-red" transform="translate(206,538) rotate(-56)">Key Performance Indicator Development</text>
    <text class="c-slate" transform="translate(247,540) rotate(-56)">Business Acquisition Due Diligence</text>
    <text class="c-olive" transform="translate(290,538) rotate(-56)">Business Strategy Consulting</text>
    <text class="c-mint" transform="translate(332,538) rotate(-56)">Internal Controls Consulting</text>
    <text class="c-tang" transform="translate(372,538) rotate(-56)">Financial Forecasting</text>
    <text class="c-slate" transform="translate(412,540) rotate(-56)">Succession Planning</text>
    <text class="c-red" transform="translate(457,538) rotate(-56)">Payroll Tax Returns</text>
    <text class="c-olive" transform="translate(499,538) rotate(-56)">Divorce Consulting</text>
    <text class="c-tang" transform="translate(542,538) rotate(-56)">Business Valuation</text>
    <text class="c-slate" transform="translate(584,538) rotate(-56)">Sales Tax Returns</text>
    <text class="c-mint" transform="translate(627,538) rotate(-56)">Budgeting</text>
  </g>
</svg>
</body>
</html>
```